Company notecard redesign

We'd like a redesign done of our company notecards. We use these cards to hand-write messages to clients/potential clients. This could be thank-you cards, congratulations cards, check-in cards, etc. Current cards are 5.5" x 8.5" and fold in half (you'll see the fold mark on the scanned image). We would like the new cards to not fold, and just be 5.5" x 4.25". We do like the little dog head you'll see on the inside notecard scan as the dog is our logo. I've also attached our "professional" logo with our new tagline. Address info you see on the outside notecard scan is correct.

Target Market(s)

Salesforce and CRM clients

Industry/Entity Type

It Company

Colors
3377b5
ffffff
fff8ef

Requirements
Must have
• Our logo, some contact info
Nice to have
• Dog head from our current notecard scan

```html
<!DOCTYPE html>
<html lang="en">
<head>
<meta charset="utf-8">
<title>Bramley Notecard – Front and Back</title>
<link href="https://fonts.googleapis.com/css2?family=Roboto:wght@700&family=Roboto+Condensed:wght@400;700&family=Open+Sans:wght@400&display=swap" rel="stylesheet">
<style>
  :root {
    --page: #ffffff;
    --label: #8e8e8e;
    --card-border: #c9c9c9;
    --watermark: #e9f0f6;
    --contact-light: #8fb6da;
    --contact-name: #c3d2de;
    --navy-deep: #031a5a;
    --navy-mid: #0b3b86;
    --blue-bright: #2b79b8;
    --logo-ink: #0a2f4d;
    --logo-dot: #7aaed0;
    --tagline: #8a8a8a;
    --white: #ffffff;
  }
  * { box-sizing: border-box; margin: 0; padding: 0; }
  html, body { width: 1200px; height: 1000px; overflow: hidden; background: var(--page); }
  .sheet { position: relative; width: 1200px; height: 1000px; }

  .side-label {
    position: absolute; top: 266px;
    font-family: "Roboto", sans-serif; font-weight: 700; font-size: 17px;
    color: var(--label); letter-spacing: 0.2px;
  }
  .side-label--front { left: 17px; }
  .side-label--back { right: 16px; }

  .card { position: absolute; top: 293px; width: 574px; height: 443px; overflow: hidden; }
  .card--front { left: 17px; background: var(--white); border: 1px solid var(--card-border); }
  .card--back { left: 610px; background: var(--navy-deep); }

  .watermark-area {
    position: absolute; left: 330px; top: 0; width: 244px; height: 252px;
    background: radial-gradient(ellipse at 60% 45%, var(--watermark) 55%, rgba(233,240,246,0) 75%);
  }

  .contact-row {
    position: absolute; display: flex; align-items: center; white-space: nowrap;
    font-family: "Roboto Condensed", sans-serif; font-size: 11px;
  }
  .contact-row .phone, .contact-row .web { font-weight: 700; }
  .contact-row .address { margin: 0 12px 0 11px; }

  .card--front .contact-row { left: 142px; top: 402px; color: var(--contact-light); }
  .mini-brand {
    position: absolute; left: 39px; top: 398px; display: flex; align-items: center; gap: 4px;
    font-family: "Roboto Condensed", sans-serif; font-weight: 700; font-size: 16px;
    color: var(--contact-name); letter-spacing: 0.5px;
  }
  .mini-brand .dot { width: 9px; height: 9px; border-radius: 50%; background: var(--contact-name); }

  .back-backdrop {
    position: absolute; inset: 0;
    background: radial-gradient(ellipse 330px 190px at 52% 45%,
      var(--white) 0%, var(--white) 78%, var(--blue-bright) 92%,
      var(--navy-mid) 108%, var(--navy-deep) 130%);
  }

  .brand-lockup { position: absolute; left: 148px; top: 149px; }
  .brand-lockup .brand-line { display: flex; align-items: center; gap: 10px; }
  .brand-name {
    font-family: "Roboto Condensed", sans-serif; font-weight: 700; font-size: 66px; line-height: 1;
    color: var(--logo-ink); letter-spacing: 2px;
  }
  .brand-mark { width: 48px; height: 48px; border-radius: 50%; background: var(--logo-dot); }
  .tagline {
    margin-top: 8px;
    font-family: "Open Sans", sans-serif; font-size: 14px; color: var(--tagline); letter-spacing: 1.6px;
  }

  .card--back .contact-row { left: 149px; top: 399px; color: var(--white); }
</style>
</head>
<body>
<main class="sheet">
  <p class="side-label side-label--front">FRONT</p>
  <p class="side-label side-label--back">BACK</p>

  <section class="card card--front">
    <div class="watermark-area" role="img" aria-label="Large faint brand mark watermark"></div>
    <div class="mini-brand"><span>BRAMLEY</span><span class="dot"></span></div>
    <div class="contact-row">
      <span class="phone">555-014-2290</span>
      <span class="address">1180 N Harbor Ave. Suite 4, Fairview, OH 44126</span>
      <span class="web">BRAMLEYTECH.com</span>
    </div>
  </section>

  <section class="card card--back">
    <div class="back-backdrop" role="img" aria-label="Decorative blue wave background around a white centre"></div>
    <div class="brand-lockup">
      <div class="brand-line">
        <span class="brand-name">BRAMLEY</span>
        <span class="brand-mark"></span>
      </div>
      <p class="tagline">A CLOUD CONSULTING COMPANY</p>
    </div>
    <div class="contact-row">
      <span class="phone">555-014-2290</span>
      <span class="address">1180 N Harbor Ave. Suite 4, Fairview, OH 44126</span>
      <span class="web">BRAMLEYTECH.com</span>
    </div>
  </section>
</main>
</body>
</html>
```